TellNearby

We are in need of a mobile app design including app and different icons.
- main page: to show
. asking or sharing (position, what I do, emotions, etc) with own contacts
. asking or sharing (what help I need) with subscribers around me
. Panic button (in case of emergency) that I can calll emergency services
(Police, Ambulance, Fire brigade, or
other personalized contacts (car relief, Insurance, my ICE contact)
Please refer to the attached PowerPoint for content and details. It shows the screens we need and explains about the branding and the approach we need.
Looking forward your proposals.

Reason: As I am new, I went for the proposed budget. Support team helped me better understand the systematic here :-)

Reason: I want to give a chance to a designer who submitted a proposal and I want to see his updated proposal per my input via email to him.

Target Market(s)

Yougsters and trendy people

Industry/Entity Type

Insurance

Font styles to use
Sans Serif

Colors
ffffff
9bcb3b

Requirements
Must have
• Should express: We are sharing, we are in a happy world, we keep in touch with each other, we are spontaneous.

Light green tendency (Brazilian light and shiny green) as a tendency.
Taking thins into account take zolta a an inspiration from the popular apps (not talking about smilies, etc..., it is about their core design approach).
Nice to have
• design complicant sharing icons (e-mail, pagenook, chirpel, SMS, etc)
Should not have
• Emergency look

```html
<!DOCTYPE html>
<html lang="en">
<head>
<meta charset="utf-8">
<title>TellNearby – App Screens</title>
<link href="https://fonts.googleapis.com/css2?family=Open+Sans:wght@400;600;700;800&display=swap" rel="stylesheet">
<style>
  :root {
    --backdrop: #eeedf1;
    --screen-white: #ffffff;
    --status-black: #0b0b0b;
    --green-light: #86e070;
    --green-mid: #5cc94a;
    --green-deep: #2f9a2c;
    --brand-text: #1f7a22;
    --band-green: #2d6a4c;
    --band-icon: #7fd39a;
    --field-fill: #efefef;
    --field-line: #dcdcdc;
    --field-text: #a8a8a8;
    --button-dark: #545454;
    --tile-teal: #1fb7a3;
    --tile-yellow: #f5c211;
    --tile-red: #ec1c1c;
    --tile-blue: #1798c3;
    --badge-red: #e8202a;
    --ink-white: #ffffff;
  }
  * { box-sizing: border-box; margin: 0; padding: 0; }
  html, body {
    width: 1200px; height: 675px; overflow: hidden;
    background: var(--backdrop);
    font-family: "Open Sans", sans-serif;
  }
  .stage { position: relative; width: 1200px; height: 675px; }
  .screen {
    position: absolute; top: 55px;
    width: 320px; height: 566px;
    background: var(--screen-white);
    border: 1px solid #2a2a2a;
    overflow: hidden;
  }
  .screen--login { left: 229px; }
  .screen--home { left: 654px; }

  .status-bar {
    position: relative;
    height: 21px; background: var(--status-black);
    color: var(--ink-white);
    display: flex; align-items: center; justify-content: space-between;
    padding: 0 6px; font-size: 11px; font-weight: 700;
  }
  .status-bar__carrier { display: flex; align-items: center; gap: 4px; }
  .status-bar__center { position: absolute; left: 50%; transform: translateX(-50%); display: flex; }

  .hero {
    position: relative;
    background: radial-gradient(circle at 45% 40%, var(--green-light) 0%, var(--green-mid) 45%, var(--green-deep) 100%);
    overflow: hidden;
  }
  .hero::after {
    content: ""; position: absolute; top: -40px; right: -120px;
    width: 260px; height: 520px;
    background: rgba(255,255,255,0.16);
    transform: rotate(28deg);
    z-index: 0;
  }
  .hero--login { height: 328px; display: flex; align-items: center; justify-content: center; }
  .brand { position: relative; z-index: 1; display: flex; align-items: center; gap: 10px; margin-top: 20px; }
  .brand__dot { width: 14px; height: 14px; border-radius: 50%; background: var(--brand-text); }
  .brand__name { font-size: 26px; font-weight: 800; color: var(--brand-text); letter-spacing: 0.5px; }

  .login-form { display: flex; flex-direction: column; align-items: center; padding-top: 23px; gap: 13px; }
  .login-form__field {
    width: 253px; height: 40px;
    background: var(--field-fill); border: 1px solid var(--field-line);
    color: var(--field-text); font-size: 12px;
    display: flex; align-items: center; padding-left: 10px;
  }
  .login-form__field--secret { letter-spacing: 2px; }
  .login-form__button {
    width: 203px; height: 40px; background: var(--button-dark);
    color: var(--ink-white); font-weight: 700; font-size: 16px;
    display: flex; align-items: center; justify-content: center;
  }

  .hero--profile { height: 179px; display: flex; align-items: center; justify-content: center; }
  .avatar {
    position: relative; z-index: 1;
    width: 120px; height: 120px; border-radius: 50%;
    border: 5px solid #2f6b3c;
    background: radial-gradient(circle at 50% 40%, #d4a788 0%, #b0b4b5 60%, #8f9597 100%);
    margin-top: 12px;
  }
  .profile-band {
    height: 60px; background: var(--band-green);
    display: flex; align-items: center; justify-content: space-between;
    padding: 0 12px 0 14px; color: var(--ink-white);
  }
  .profile-band__name { font-size: 21px; font-weight: 600; line-height: 1.1; }
  .profile-band__place { font-size: 13px; padding-left: 3px; }

  .tile-grid {
    display: grid; grid-template-columns: 141px 141px; gap: 10px;
    padding: 12px 0 0 13px;
  }
  .tile {
    height: 131px; position: relative; color: var(--ink-white);
    display: flex; flex-direction: column; align-items: center; justify-content: flex-end;
    padding-bottom: 9px; text-align: center;
  }
  .tile--share { background: var(--tile-teal); }
  .tile--help { background: var(--tile-yellow); }
  .tile--panic { background: var(--tile-red); }
  .tile--contacts { background: var(--tile-blue); }
  .tile__icon { position: absolute; top: 22px; left: 50%; transform: translateX(-50%); }
  .tile__title { font-size: 14px; font-weight: 600; line-height: 1.15; }
  .tile__note { font-size: 7.5px; line-height: 1.2; }
  .tile__scene {
    position: absolute; top: 16px; left: 50%; transform: translateX(-50%);
    width: 90px; height: 62px;
    background: linear-gradient(180deg, rgba(255,255,255,0.35), rgba(255,255,255,0.15));
    border-radius: 4px;
  }
  .badge {
    position: absolute; top: -6px; right: -8px;
    width: 16px; height: 16px; border-radius: 50%;
    background: var(--badge-red); border: 1.5px solid #fff;
    font-size: 9px; font-weight: 700; display: flex; align-items: center; justify-content: center;
  }
</style>
</head>
<body>
<main class="stage">

  <section class="screen screen--login">
    <div class="status-bar">
      <span class="status-bar__carrier">
        <svg width="14" height="8" viewBox="0 0 14 8"><rect x="0" y="6" width="2" height="2" fill="#fff"/><rect x="3" y="4" width="2" height="4" fill="#fff"/><rect x="6" y="2" width="2" height="6" fill="#fff"/><rect x="9" y="0" width="2" height="8" fill="#fff"/></svg>
        CARRIER
      </span>
      <span class="status-bar__center"><svg width="9" height="11" viewBox="0 0 9 11"><path d="M2 5V3.5a2.5 2.5 0 0 1 5 0V5" stroke="#fff" stroke-width="1.4" fill="none"/><rect x="0.5" y="5" width="8" height="6" fill="#fff"/></svg></span>
      <svg width="18" height="9" viewBox="0 0 18 9"><rect x="0.5" y="0.5" width="15" height="8" stroke="#fff" fill="none"/><rect x="2" y="2" width="12" height="5" fill="#fff"/><rect x="16" y="3" width="2" height="3" fill="#fff"/></svg>
    </div>
    <div class="hero hero--login">
      <div class="brand">
        <span class="brand__dot"></span>
        <span class="brand__name">TellNearby</span>
      </div>
    </div>
    <form class="login-form">
      <div class="login-form__field">User Name</div>
      <div class="login-form__field login-form__field--secret">●●●●●●●●●</div>
      <div class="login-form__button">Login</div>
    </form>
  </section>

  <section class="screen screen--home">
    <div class="status-bar">
      <span class="status-bar__carrier">
        <svg width="14" height="8" viewBox="0 0 14 8"><rect x="0" y="6" width="2" height="2" fill="#fff"/><rect x="3" y="4" width="2" height="4" fill="#fff"/><rect x="6" y="2" width="2" height="6" fill="#fff"/><rect x="9" y="0" width="2" height="8" fill="#fff"/></svg>
        CARRIER
      </span>
      <span class="status-bar__center"><svg width="9" height="11" viewBox="0 0 9 11"><path d="M2 5V3.5a2.5 2.5 0 0 1 5 0V5" stroke="#fff" stroke-width="1.4" fill="none"/><rect x="0.5" y="5" width="8" height="6" fill="#fff"/></svg></span>
      <svg width="18" height="9" viewBox="0 0 18 9"><rect x="0.5" y="0.5" width="15" height="8" stroke="#fff" fill="none"/><rect x="2" y="2" width="12" height="5" fill="#fff"/><rect x="16" y="3" width="2" height="3" fill="#fff"/></svg>
    </div>
    <div class="hero hero--profile">
      <div class="avatar" role="img" aria-label="Profile photo of the user"></div>
    </div>
    <div class="profile-band">
      <div>
        <div class="profile-band__name">Marcus</div>
        <div class="profile-band__place">Florida</div>
      </div>
      <svg class="profile-band__message" width="44" height="30" viewBox="0 0 44 30" aria-label="Messages">
        <path d="M0 2h44v20H10l-6 8V22H0z" fill="var(--band-icon)"/>
        <rect x="9" y="8" width="22" height="2.5" fill="var(--band-green)"/>
        <rect x="9" y="13" width="15" height="2.5" fill="var(--band-green)"/>
      </svg>
    </div>

    <div class="tile-grid">
      <div class="tile tile--share">
        <div class="tile__icon">
          <svg width="40" height="36" viewBox="0 0 40 36"><circle cx="20" cy="18" r="15" fill="none" stroke="#fff" stroke-width="3"/></svg>
          <span class="badge">2</span>
        </div>
        <div class="tile__title">Asking or Sharing</div>
        <div class="tile__note">position, what I do, emotions, etc</div>
      </div>
      <div class="tile tile--help">
        <svg class="tile__icon" width="40" height="52" viewBox="0 0 40 52" aria-label="Location pin">
          <path d="M20 2C10 2 3 9.5 3 19c0 12 17 31 17 31s17-19 17-31C37 9.5 30 2 20 2z" fill="#fff"/>
          <circle cx="20" cy="19" r="7" fill="var(--tile-yellow)"/>
        </svg>
        <div class="tile__title">Need Help</div>
        <div class="tile__note">with subscribers around me</div>
      </div>
      <div class="tile tile--panic">
        <div class="tile__scene" role="img" aria-label="Illustration of two alarmed people calling for help"></div>
        <div class="tile__title">Panic</div>
        <div class="tile__note">Police, Ambulance, Fire brigade</div>
      </div>
      <div class="tile tile--contacts">
        <svg class="tile__icon" width="48" height="48" viewBox="0 0 24 24" aria-label="Phone">
          <path d="M6.6 10.8a15.2 15.2 0 0 0 6.6 6.6l2.2-2.2c.3-.3.7-.4 1-.2 1.1.4 2.3.6 3.6.6.6 0 1 .4 1 1V20c0 .6-.4 1-1 1C10.6 21 3 13.4 3 4c0-.6.4-1 1-1h3.5c.6 0 1 .4 1 1 0 1.3.2 2.5.6 3.6.1.3 0 .7-.2 1z" fill="#fff"/>
        </svg>
        <div class="tile__title">other contacts</div>
        <div class="tile__note">car relief, Insurance, my ICE contact</div>
      </div>
    </div>
  </section>

</main>
</body>
</html>
```